Portfolio required for virtual assistant seeking new clients

I require an editable Word template that can be sent to clients. This is a new business venture I am undertaking - working as a virtual assistant (administration work). I will need to find my own clients so would like Wow factor. Target group will be small businesses/legal industry so needs to look professional.
The portfolio will need to note information about me, why hire me, my skill set and credentials. May add testimonials too. I have attached a draft of the amount of text required - still working on this.
I will upload my logo and business card design. I do like consistency.
Colours used Pantone 2745 C and 272 C. Open to other colours but would like to see the main colours of logo incorporated. Images welcome. May insert an image of myself at some stage so please allow for a spot for this photo.
The portfolio will need to be converted to pdf to send by email as well as printable.
Updates

Automatically set for 24 hours apologies did not see this. Now amended

```html
<!DOCTYPE html>
<html lang="en">
<head>
<meta charset="utf-8">
<title>Mara Quill Virtual Assistant – Portfolio</title>
<link rel="stylesheet" href="https://fonts.googleapis.com/css2?family=Barlow:wght@400;500;600;700&family=Lato:wght@300;400;700;900&display=swap">
<style>
  :root{
    --navy:#2e3a8c;
    --lilac:#7b85c4;
    --mist:#e4e6f3;
    --card-line:#b9bde3;
    --ink:#2b2b2b;
    --backdrop:#2b2b2b;
    --white:#ffffff;
  }
  *{margin:0;padding:0;box-sizing:border-box}
  html,body{width:1200px;height:1200px;overflow:hidden;background:var(--backdrop)}
  body{position:relative;font-family:"Barlow",sans-serif;color:var(--ink)}
  .page{position:absolute;top:244px;width:538px;height:755px;background:var(--white);overflow:hidden}
  .page--profile{left:44px}
  .page--services{left:618px}

  /* ---------- profile page ---------- */
  .profile-band{position:absolute;left:0;top:0;width:100%;height:188px;background:var(--navy)}
  .sidebar{position:absolute;left:25px;top:113px;width:214px;height:583px;background:var(--lilac)}
  .photo-slot{position:absolute;left:55px;top:31px;width:160px;height:159px;background:var(--white)}
  .brand{position:absolute;left:255px;top:122px;width:270px;text-align:center;color:var(--white);font-family:"Lato",sans-serif}
  .brand__name{font-weight:400;font-size:25px;letter-spacing:5px;line-height:1}
  .brand__role{font-weight:300;font-size:14px;letter-spacing:3.2px;margin-top:6px}

  .tag{position:absolute;height:26px;border:1.5px solid;font-family:"Lato",sans-serif;font-weight:900;font-size:12.5px;letter-spacing:3px;display:flex;align-items:center;justify-content:center}
  .tag--light{left:64px;top:212px;width:145px;border-color:var(--white);color:var(--white)}
  .tag--dark{border-color:var(--navy);color:var(--navy);background:var(--white)}

  .why-intro{position:absolute;left:40px;top:250px;width:186px;color:var(--white);font-size:13px;font-weight:500;line-height:14.2px;text-align:center}
  .why-list{position:absolute;left:34px;top:417px;width:196px;list-style:none;color:var(--white);font-size:10.2px;line-height:13px}
  .why-list li{display:flex;gap:6px;margin-bottom:12px}
  .why-list svg{flex:0 0 13px;width:13px;height:13px;margin-top:0}

  .about{position:absolute;left:266px;top:244px;width:245px;font-size:10.4px;line-height:13.1px;text-align:justify}
  .about p{margin-bottom:13px}
  .credentials{position:absolute;left:268px;top:646px;list-style:none;font-size:10.4px;font-weight:600;line-height:13px}
  .credentials li::before{content:"•";color:var(--lilac);margin-right:5px}

  .footer{position:absolute;left:0;bottom:0;width:100%;height:41px;display:flex;align-items:center;font-size:10px;font-weight:600}
  .footer--light{background:var(--mist);color:var(--navy)}
  .footer--dark{background:var(--navy);color:var(--white)}
  .footer__abn{position:absolute;left:55px}
  .footer__item{position:absolute;display:flex;align-items:center;gap:8px}
  .footer__item svg{width:14px;height:14px}

  /* ---------- services page ---------- */
  .services-head{position:absolute;left:0;top:0;width:100%;height:116px;display:flex}
  .services-head__brand{width:168px;background:var(--navy);color:var(--white);font-family:"Lato",sans-serif;text-align:center;padding-top:48px}
  .services-head__brand .brand__name{font-size:15px;letter-spacing:3px}
  .services-head__brand .brand__role{font-size:8.5px;letter-spacing:1.8px;margin-top:4px}
  .services-head__title{flex:1;background:var(--lilac);color:var(--white);font-family:"Lato",sans-serif;font-weight:900;font-size:22px;display:flex;align-items:center;padding-left:42px}

  .card{position:absolute;width:236px;border:1.5px solid var(--card-line);padding:6px 8px}
  .card__head{display:flex;align-items:center;gap:8px;min-height:42px}
  .card__icon{flex:0 0 42px;width:42px;height:42px;background:var(--lilac)}
  .card__title{font-weight:700;font-size:13px;line-height:14px;color:var(--navy)}
  .card__list{list-style:none;font-size:10.8px;line-height:13px;margin:6px 0 0 9px}
  .card__list li{padding-left:8px;position:relative}
  .card__list li::before{content:"";position:absolute;left:0;top:5px;width:3px;height:3px;border-radius:50%;background:var(--lilac)}
  .col-a{left:28px}.col-b{left:277px}
  .row-1{top:137px;height:189px}
  .row-2{top:338px;height:108px}
  .row-3{top:456px;height:110px}
  .row-4{top:576px;height:110px}
  .credit{position:absolute;left:46px;top:696px;font-size:6.5px;color:#666}
</style>
</head>
<body>

<section class="page page--profile">
  <div class="profile-band"></div>
  <div class="sidebar"></div>
  <div class="photo-slot" role="img" aria-label="Space for a portrait photo"></div>
  <div class="brand">
    <div class="brand__name">MARA QUILL</div>
    <div class="brand__role">VIRTUAL ASSISTANT</div>
  </div>

  <div class="tag tag--light">WHY HIRE ME</div>
  <p class="why-intro">A virtual assistant is an affordable alternative to hiring on-site administration support. Hire me for a once-off task or on a regular basis. I'm here to help you so get more time back in your day so you can focus on more important tasks. I want to save you time, as who has enough of that these days!</p>

  <ul class="why-list">
    <li><svg viewBox="0 0 14 14"><circle cx="7" cy="7" r="6" fill="none" stroke="#fff" stroke-width="1.2"/><path d="M4 7.2l2 2 4.5-4.6" fill="none" stroke="#fff" stroke-width="1.5"/></svg><span>I am known for my reliability, determination, ability to work diligently in fast-paced environments as well as delivering results.</span></li>
    <li><svg viewBox="0 0 14 14"><circle cx="7" cy="7" r="6" fill="none" stroke="#fff" stroke-width="1.2"/><path d="M4 7.2l2 2 4.5-4.6" fill="none" stroke="#fff" stroke-width="1.5"/></svg><span>I take pride in my meticulous approach to the tasks I undertake.</span></li>
    <li><svg viewBox="0 0 14 14"><circle cx="7" cy="7" r="6" fill="none" stroke="#fff" stroke-width="1.2"/><path d="M4 7.2l2 2 4.5-4.6" fill="none" stroke="#fff" stroke-width="1.5"/></svg><span>I adapt well to new technology.</span></li>
    <li><svg viewBox="0 0 14 14"><circle cx="7" cy="7" r="6" fill="none" stroke="#fff" stroke-width="1.2"/><path d="M4 7.2l2 2 4.5-4.6" fill="none" stroke="#fff" stroke-width="1.5"/></svg><span>I am excited to embrace new opportunities that allow me to showcase my skill set expertise, provide dedicated support to professionals and that may involve my legal expertise.</span></li>
    <li><svg viewBox="0 0 14 14"><circle cx="7" cy="7" r="6" fill="none" stroke="#fff" stroke-width="1.2"/><path d="M4 7.2l2 2 4.5-4.6" fill="none" stroke="#fff" stroke-width="1.5"/></svg><span>I am committed to making a positive impact wherever I go, bringing efficiency and structure.</span></li>
  </ul>

  <div class="tag tag--dark" style="left:319px;top:210px;width:147px">ABOUT ME</div>
  <div class="about">
    <p>Hello, I'm Mara Quill, a mother, coffee lover, and a passion for travel. I enjoy organisation and making life easy. With over 15 years of experience in the legal field, I have gained valuable experience whilst at the same time, perfecting my skills.</p>
    <p>Throughout my journey in the legal profession, I have held various roles, each contributing to my growth and expertise. Starting as a Rounds Clerk, I quickly advanced to the role of Administrative Assistant in the area of Litigation which involved leading a team of administration assistants focused on supporting legal professionals and litigation processes.</p>
    <p>This role was invaluable in that it taught me the importance of organisation, time management, attention to detail and multitasking. I then transitioned into Debt Recovery, where I thrived as a Paralegal. In this role, I took on the responsibility of managing my own case load and providing comprehensive legal support independently.</p>
    <p>Attention to detail, meticulous research and effective communication became second nature. This allowed me to achieve successful resolutions while maintaining the utmost organization and professionalism.</p>
  </div>

  <div class="tag tag--dark" style="left:316px;top:612px;width:147px">CREDENTIALS</div>
  <ul class="credentials">
    <li>Certificate IV in Business (Legal Services)</li>
    <li>Certificate III of Business Administration</li>
    <li>Certificate II in Business</li>
  </ul>

  <footer class="footer footer--light">
    <span class="footer__abn">ABN</span>
    <span class="footer__item" style="left:186px"><svg viewBox="0 0 14 14"><circle cx="7" cy="7" r="7" fill="#2e3a8c"/><path d="M4.6 3.8l1.5-.3.8 1.9-.9.7a5 5 0 0 0 2 2l.7-.9 1.9.8-.3 1.5c-3.2.2-6-2.5-5.7-5.7z" fill="#fff"/></svg>0491 570 118</span>
    <span class="footer__item" style="left:393px"><svg viewBox="0 0 14 14"><circle cx="7" cy="7" r="7" fill="#2e3a8c"/><rect x="3.6" y="4.6" width="6.8" height="4.8" fill="#fff"/><path d="M3.6 4.8L7 7.4l3.4-2.6" fill="none" stroke="#2e3a8c" stroke-width=".8"/></svg>mara@mqva.com.au</span>
  </footer>
</section>

<section class="page page--services">
  <header class="services-head">
    <div class="services-head__brand">
      <div class="brand__name">MARA QUILL</div>
      <div class="brand__role">VIRTUAL ASSISTANT</div>
    </div>
    <h1 class="services-head__title">WHAT CAN I DO FOR YOU?</h1>
  </header>

  <article class="card col-a row-1">
    <div class="card__head"><div class="card__icon" role="img" aria-label="Administration icon"></div><h2 class="card__title">GENERAL ADMINISTRATION SUPPORT</h2></div>
    <ul class="card__list">
      <li>Document preparation including editing and formatting</li>
      <li>Spreadsheets</li>
      <li>Client correspondence</li>
      <li>Customer service / telephone calls</li>
      <li>Invoicing</li>
      <li>Bulk mail outs</li>
      <li>Data entry</li>
      <li>Database and records management</li>
    </ul>
  </article>

  <article class="card col-b row-1">
    <div class="card__head"><div class="card__icon" role="img" aria-label="Debt collection icon"></div><h2 class="card__title">DEBT COLLECTION</h2></div>
    <ul class="card__list">
      <li>Assist with sending out overdue statements</li>
      <li>Issue demand letters</li>
      <li>Issue Claims and enforcement action in the Magistrates Court of Westhaven</li>
      <li>Negotiating payment arrangements</li>
      <li>Knowledge with Courtvane portal</li>
    </ul>
  </article>

  <article class="card col-a row-2">
    <div class="card__head"><div class="card__icon" role="img" aria-label="Email icon"></div><h2 class="card__title">EMAIL MANAGEMENT</h2></div>
    <ul class="card__list">
      <li>Categorize and prepare sub folders</li>
      <li>Prioritize emails</li>
      <li>Send email correspondence</li>
    </ul>
  </article>

  <article class="card col-b row-2">
    <div class="card__head"><div class="card__icon" role="img" aria-label="Software icon"></div><h2 class="card__title">SOFTWARE</h2></div>
    <ul class="card__list">
      <li>Deskwren 365</li>
      <li>Caselore Affinity</li>
      <li>LEDGRA</li>
    </ul>
  </article>

  <article class="card col-a row-3">
    <div class="card__head"><div class="card__icon" role="img" aria-label="Calendar icon"></div><h2 class="card__title">CALENDAR &amp;<br>DIARY MANAGEMENT</h2></div>
    <ul class="card__list">
      <li>Assist with scheduling appointments and meetings</li>
      <li>Scheduling reminders</li>
    </ul>
  </article>

  <article class="card col-b row-3">
    <div class="card__head"><div class="card__icon" role="img" aria-label="Legal documents icon"></div><h2 class="card__title">LEGAL</h2></div>
    <ul class="card__list">
      <li>Courtvane portal</li>
      <li>Preparing Court documents</li>
      <li>Filing Court Documents</li>
    </ul>
  </article>

  <article class="card col-a row-4">
    <div class="card__head"><div class="card__icon" role="img" aria-label="Travel luggage icon"></div><h2 class="card__title">TRAVEL ARRANGEMENTS</h2></div>
    <ul class="card__list">
      <li>Assist with booking intrastate/ interstate travel</li>
      <li>Assist with car hire and accommodation</li>
    </ul>
  </article>

  <article class="card col-b row-4">
    <div class="card__head"><div class="card__icon" role="img" aria-label="Other services icon"></div><h2 class="card__title">OTHER</h2></div>
    <ul class="card__list">
      <li>Online research</li>
      <li>Event coordination</li>
    </ul>
  </article>

  <p class="credit">Icons by Iconsmith from Glyphbank.com</p>

  <footer class="footer footer--dark">
    <span class="footer__abn">ABN</span>
    <span class="footer__item" style="left:186px"><svg viewBox="0 0 14 14"><circle cx="7" cy="7" r="7" fill="#fff"/><path d="M4.6 3.8l1.5-.3.8 1.9-.9.7a5 5 0 0 0 2 2l.7-.9 1.9.8-.3 1.5c-3.2.2-6-2.5-5.7-5.7z" fill="#2e3a8c"/></svg>0491 570 118</span>
    <span class="footer__item" style="left:393px"><svg viewBox="0 0 14 14"><circle cx="7" cy="7" r="7" fill="#fff"/><rect x="3.6" y="4.6" width="6.8" height="4.8" fill="#2e3a8c"/><path d="M3.6 4.8L7 7.4l3.4-2.6" fill="none" stroke="#fff" stroke-width=".8"/></svg>mara@mqva.com.au</span>
  </footer>
</section>

</body>
</html>
```